GDFH Business Card

Looking for a business card design to incorporate our branding. We want to only use the colors listing in the Branding Package (attached).
Updates

Target Market(s)

People who need their phone or device fixed.

Industry/Entity Type

Electronics

Contact Information for Business Card

Please use:

Gadget Fix Haven LLC
4870 S Ridgecrest Pkwy
Suite 318
San Antonio, TX 78291

Wendell Thorsby, Store Manager

(210) 555-0147

Requirements
Must have
• Must include the colors that are contained within the Branding Package PDF file.

```html
<!DOCTYPE html>
<html lang="en">
<head>
<meta charset="utf-8">
<title>Gadget Fix Haven – Business Card</title>
<link href="https://fonts.googleapis.com/css2?family=Open+Sans:wght@400;700&display=swap" rel="stylesheet">
<style>
  :root {
    --orange: #ee5424;
    --yellow: #f7b52a;
    --white: #ffffff;
    --ink: #4a4a4a;
    --backdrop: #e4e4e4;
  }
  * { box-sizing: border-box; margin: 0; padding: 0; }
  html, body { width: 1200px; height: 1200px; overflow: hidden; }
  body {
    background: var(--backdrop);
    font-family: "Open Sans", Arial, sans-serif;
    position: relative;
  }
  .card {
    position: absolute;
    left: 180px;
    width: 840px;
    height: 480px;
    overflow: hidden;
    box-shadow: 0 8px 24px rgba(0,0,0,0.18);
  }
  .card--front { top: 90px; background: var(--white); }
  .card--back { top: 630px; background: var(--orange); }

  .panel {
    position: absolute;
    left: -40px;
    top: 30px;
    width: 840px;
    height: 420px;
    border: 6px solid var(--yellow);
    border-radius: 0 60px 60px 0;
  }
  .card--front .panel { background: var(--orange); }
  .card--back .panel { background: var(--white); }

  .contact {
    position: absolute;
    left: 80px;
    top: 90px;
    right: 80px;
    color: var(--white);
  }
  .contact__name {
    font-weight: 700;
    font-size: 36px;
    letter-spacing: 1px;
    text-transform: uppercase;
  }
  .contact__title { font-size: 22px; margin: 4px 0 0 26px; }
  .contact__rule {
    border: 0;
    border-top: 1.5px solid var(--white);
    margin: 18px 0 0 26px;
    width: 640px;
  }
  .contact__company { font-size: 22px; margin: 40px 0 0 100px; }
  .contact__rule--short { width: 250px; margin: 8px 0 0 100px; }
  .contact__line {
    display: flex;
    align-items: center;
    gap: 8px;
    font-size: 22px;
    margin: 10px 0 0 100px;
  }
  .contact__line svg { width: 26px; height: 26px; fill: var(--white); flex: none; }

  .brand {
    position: absolute;
    left: 0; right: 0; top: 0; bottom: 0;
    display: flex;
    align-items: center;
    justify-content: center;
    gap: 22px;
  }
  .brand__mark {
    width: 64px; height: 64px;
    background: var(--orange);
    border-radius: 10px;
  }
  .brand__name {
    color: var(--orange);
    font-size: 52px;
    font-weight: 400;
  }
</style>
</head>
<body>
  <section class="card card--front" aria-label="Business card front">
    <div class="panel"></div>
    <div class="contact">
      <h1 class="contact__name">Wendell Thorsby</h1>
      <p class="contact__title">Store Manager</p>
      <hr class="contact__rule">
      <p class="contact__company">Gadget Fix Haven LLC</p>
      <hr class="contact__rule contact__rule--short">
      <p class="contact__line">
        <svg viewBox="0 0 24 24" aria-hidden="true"><path d="M3 8c0-2 4-4 9-4s9 2 9 4v2h-5V8.5c-2-.7-6-.7-8 0V10H3z"/><path d="M6 11h12l2 8H4z"/><circle cx="12" cy="15" r="2.5" fill="#ee5424"/></svg>
        (210) 555-0147
      </p>
      <p class="contact__line">
        <svg viewBox="0 0 24 24" aria-hidden="true"><path d="M12 2a7 7 0 0 0-7 7c0 5 7 13 7 13s7-8 7-13a7 7 0 0 0-7-7zm0 10a3 3 0 1 1 0-6 3 3 0 0 1 0 6z"/></svg>
        4870 S Ridgecrest Pkwy, Suite 318, San Antonio, TX 78291
      </p>
    </div>
  </section>

  <section class="card card--back" aria-label="Business card back">
    <div class="panel"></div>
    <div class="brand">
      <span class="brand__mark" aria-hidden="true"></span>
      <span class="brand__name">Gadget Fix Haven</span>
    </div>
  </section>
</body>
</html>
```